Brochure design for moving and cleaning company

Hello

We need a NEW design of our brochure that we already have. Please check the brochure and give us a creative, professional and new design of it.

Here the brochure:

https://www.filecrate.example/s/ab3kd9x2lq7mzw1/0-1Brosura%20Trasko%20Mail4.9.17%20Trasko%202014%20Kopie%202.indd?dl=0

https://www.filecrate.example/s/pz8rt4vnw2hsy6e/2016%20Druck%201%20Brosura%202016%20Brosch%C3%BCre%20Druck.pdf?dl=0

I added the new text for the brochure and new logos and pictures.

Kind regards

T. Varnesh

Industry/Entity Type

Moving Company

Colors
ec1f27

Requirements
Must have
• http://lumofrex.example/red-brochure-template/red-brochure-template-red-and-white-corporate-brochure-template-vector-free-download-free/
Nice to have

```html
<!DOCTYPE html>
<html lang="de">
<head>
<meta charset="utf-8">
<title>Umzugsdienstleistungen – Broschürenseite</title>
<link rel="stylesheet" href="https://fonts.googleapis.com/css2?family=Lato:wght@400;700&display=swap">
<style>
  :root {
    --stage: #cdcccd;
    --brand-red: #ec1f27;
    --band-top: #c9141b;
    --band-bottom: #f2545a;
    --heading-red: #d5161e;
    --ink: #1b1b1b;
    --bullet-grey: #444;
    --wine-deep: #5e0a0e;
    --wine: #9c1118;
    --wave-light: #f8c3c5;
    --wave-line: #ffffff;
    --ring-light: #f6aeb1;
    --ring-dark: #7d0d12;
    --white: #ffffff;
  }
  html, body {
    margin: 0;
    padding: 0;
    width: 1051px;
    height: 1200px;
    overflow: hidden;
    background: var(--stage);
    font-family: "Lato", sans-serif;
  }
  .page {
    position: absolute;
    left: 104px;
    top: 5px;
    width: 842px;
    height: 1190px;
    overflow: hidden;
    background: linear-gradient(90deg, #f1f1f2 0%, #ffffff 35%, #ffffff 65%, #ececee 100%);
  }
  .top-band {
    position: absolute;
    left: 0; top: 0;
    width: 100%; height: 32px;
    background: linear-gradient(180deg, var(--band-top), var(--band-bottom));
  }
  .backdrop {
    position: absolute;
    left: 0; top: 0;
  }
  .section-title {
    position: absolute;
    left: 82px;
    margin: 0;
    font-weight: 700;
    font-size: 27px;
    letter-spacing: -0.2px;
    white-space: nowrap;
  }
  .private .section-title { top: 66px; color: var(--heading-red); }
  .business .section-title { top: 863px; color: var(--white); }
  .service-list {
    position: absolute;
    margin: 0;
    padding: 0;
    list-style: none;
    font-size: 18.5px;
    line-height: 23.8px;
  }
  .service-list li {
    position: relative;
    white-space: nowrap;
  }
  .service-list li::before {
    content: "";
    position: absolute;
    top: 6px;
    width: 12px;
    height: 12px;
    border-radius: 50%;
  }
  .private .service-list {
    left: 115px;
    top: 133px;
    color: var(--ink);
  }
  .private .service-list li::before { left: -34px; background: var(--bullet-grey); }
  .business .service-list {
    left: 104px;
    top: 914px;
    color: var(--white);
  }
  .business .service-list li::before { left: -22px; background: var(--white); }
  .photo {
    position: absolute;
    border-radius: 50%;
    box-sizing: border-box;
    border: 5px solid var(--ring-dark);
    box-shadow: 0 0 0 8px var(--ring-light);
  }
  .photo-stairs-small {
    left: 40px; top: 467px; width: 198px; height: 198px;
    background: linear-gradient(160deg, #e7e3dc 0%, #b9b4ab 45%, #4fb6c9 60%, #7d7a72 100%);
  }
  .photo-wrapping {
    left: 229px; top: 570px; width: 246px; height: 246px;
    background: linear-gradient(160deg, #f2ece0 0%, #d7c6a8 40%, #3aa8c8 55%, #6b5a45 100%);
  }
  .photo-stairs-large {
    left: 463px; top: 404px; width: 342px; height: 342px;
    background: linear-gradient(160deg, #dcd8d0 0%, #a9a59c 40%, #44b3cb 58%, #86837b 100%);
  }
</style>
</head>
<body>
  <main class="page">
    <div class="top-band"></div>

    <svg class="backdrop" width="842" height="1190" viewBox="0 0 842 1190" aria-hidden="true">
      <defs>
        <radialGradient id="deep-red" cx="0.78" cy="0.45" r="0.9">
          <stop offset="0" stop-color="#ec1f27"/>
          <stop offset="0.55" stop-color="#9c1118"/>
          <stop offset="1" stop-color="#5e0a0e"/>
        </radialGradient>
      </defs>
      <path d="M0,642 C230,575 520,545 842,505 L842,1190 L0,1190 Z" fill="#f8c3c5"/>
      <path d="M0,673 C250,600 540,560 842,518" fill="none" stroke="#ffffff" stroke-width="7"/>
      <path d="M0,685 C260,618 540,580 842,560 L842,1190 L0,1190 Z" fill="url(#deep-red)"/>
    </svg>

    <section class="private">
      <h2 class="section-title">Privatumzüge: Unsere Dienstleistungen für Sie :</h2>
      <ul class="service-list">
        <li>Kostenlose Beratung, Ortsbesichtigung und Bestandsaufnahme.</li>
        <li>Montage – professionelle Demontage sowie Montage Ihrer Möbel<br>und Einrichtungen.</li>
        <li>Packservice – Falls erwünscht, packen wir Ihre empfindlichen Gegenstände<br>fachmännisch ein und wieder aus.</li>
        <li>Umzugszubehör – Wir haben für unsere Kunden das nötige Zubehör zum<br>Kauf oder\ zur Miete.</li>
        <li>Reinigungen mit Abgabegarantie und Handwerkerservice</li>
        <li>Möbeleinlagerung – Bei Bedarf können Sie bei uns auch Ihre Möbel/<br>Umzugsgut zwischenlagern (kurz- oder längerfristig).</li>
      </ul>
    </section>

    <div class="photo photo-stairs-small" role="img" aria-label="Zwei Umzugshelfer tragen ein verpacktes Möbelstück eine Treppe hinauf"></div>
    <div class="photo photo-wrapping" role="img" aria-label="Umzugshelfer umwickelt ein Möbelstück mit Stretchfolie"></div>
    <div class="photo photo-stairs-large" role="img" aria-label="Zwei Umzugshelfer tragen ein in Folie verpacktes Möbelstück die Eingangstreppe hinauf"></div>

    <section class="business">
      <h2 class="section-title">Geschäftsumzüge Dienstleistungen :</h2>
      <ul class="service-list">
        <li>Planung des Umzugsprojekts</li>
        <li>Professionelles Umzugsmanagement</li>
        <li>Termingerechter Umzugstransport</li>
        <li>Packservice mit speziellen Verpackungsutensilien</li>
        <li>Demontage und Montage von Möbeln und Einrichtungen</li>
        <li>Reinigungs- und Handwerkerservice</li>
        <li>Bei Bedarf Zwischenlagerung Ihres Umzugsgutes</li>
      </ul>
    </section>
  </main>
</body>
</html>
```